Attention grabbing 6x9 postcard

We are looking to have an attention grabbing post card that be sent out to homeowners from our roofing company Vell Roofing. the concept is that on the front it will say something like (STOP THE KNOCKING!
Tired of roofers knocking on your door? Contact us because we value your time as much as you value the roof over your head."
Vell Roofing
VellRoofing.example
555.672.VELL
info@vellroofing.example

Please feel free to come up with something very creative. Once we pick the final design we will provide the copy.

```html
<!DOCTYPE html>
<html lang="en">
<head>
<meta charset="utf-8">
<title>Vell Roofing Postcard</title>
<link rel="stylesheet" href="https://fonts.googleapis.com/css2?family=Josefin+Sans:wght@400;600&display=swap">
<style>
  :root {
    --backdrop: #e4e5e7;
    --paper: #ffffff;
    --ink: #0a0a0a;
    --rule: #333333;
    --on-photo: #ffffff;
  }
  html, body {
    margin: 0;
    width: 1200px;
    height: 1200px;
    overflow: hidden;
    background: var(--backdrop);
  }
  .sheet {
    width: 1200px;
    height: 1200px;
    display: flex;
    flex-direction: column;
    align-items: center;
    justify-content: center;
    gap: 44px;
  }
  .postcard {
    display: block;
    width: 790px;
    height: 525px;
    background: var(--paper);
  }
  .postcard text {
    font-family: "Josefin Sans", sans-serif;
  }
  .band { fill: var(--ink); }
  .brand-name { fill: var(--ink); font-weight: 600; letter-spacing: 1px; }
  .brand-mark { fill: var(--ink); }
  .brand-url { fill: var(--ink); font-weight: 600; letter-spacing: 0.6px; }
  .contact-title { fill: var(--on-photo); font-weight: 600; letter-spacing: 0.8px; }
  .contact-line { fill: var(--on-photo); font-weight: 400; }
  .stamp-box { fill: none; stroke: var(--rule); stroke-width: 1.4; }
  .address-line { stroke: var(--rule); stroke-width: 1; }
</style>
</head>
<body>
<main class="sheet">

  <!-- Front of postcard -->
  <svg class="postcard postcard-front" viewBox="0 0 632 420" xmlns="http://www.w3.org/2000/svg">
    <defs>
      <linearGradient id="front-house-tone" x1="0" y1="0" x2="0.3" y2="1">
        <stop offset="0" stop-color="#9fb6cc"/>
        <stop offset="0.35" stop-color="#5d6064"/>
        <stop offset="0.7" stop-color="#8f887f"/>
        <stop offset="1" stop-color="#9a8e80"/>
      </linearGradient>
      <linearGradient id="front-shingle-tone" x1="0" y1="0" x2="1" y2="1">
        <stop offset="0" stop-color="#6b6c6e"/>
        <stop offset="1" stop-color="#3f4042"/>
      </linearGradient>
    </defs>

    <rect width="632" height="420" fill="#ffffff"/>

    <g role="img" aria-label="Photo of a house gable with grey roof shingles and siding under a blue sky">
      <polygon points="0,164 226,292 174,420 0,420" fill="url(#front-house-tone)"/>
    </g>

    <polygon class="band" points="384,0 542,0 302,420 174,420"/>

    <g role="img" aria-label="Close-up photo of dark asphalt roof shingles">
      <polygon points="474,116 632,116 632,420 420,420 372,326" fill="url(#front-shingle-tone)"/>
    </g>

    <rect class="brand-mark" x="100" y="82" width="12" height="12"/>
    <text class="brand-name" x="120" y="94" font-size="20">VELL ROOFING</text>
    <text class="brand-url" x="172" y="174" font-size="15.5" text-anchor="middle">VELLROOFING.EXAMPLE</text>

    <text class="contact-title" x="598" y="229" font-size="17" text-anchor="end">VELL ROOFING</text>
    <text class="contact-line" x="598" y="285" font-size="15.5" text-anchor="end">VellRoofing.example</text>
    <text class="contact-line" x="598" y="312" font-size="15.5" text-anchor="end">555.672.VELL</text>
    <text class="contact-line" x="598" y="338" font-size="15.5" text-anchor="end">info@vellroofing.example</text>
  </svg>

  <!-- Back of postcard -->
  <svg class="postcard postcard-back" viewBox="0 0 632 420" xmlns="http://www.w3.org/2000/svg">
    <defs>
      <linearGradient id="back-house-tone" x1="0" y1="0" x2="0.3" y2="1">
        <stop offset="0" stop-color="#6e7278"/>
        <stop offset="0.5" stop-color="#55585c"/>
        <stop offset="1" stop-color="#5f5d5a"/>
      </linearGradient>
    </defs>

    <rect width="632" height="420" fill="#ffffff"/>

    <g role="img" aria-label="Darkened photo of a house gable with roof shingles">
      <polygon points="0,126 250,256 184,420 0,420" fill="url(#back-house-tone)"/>
    </g>

    <polygon class="band" points="363,0 436,0 196,420 178,420"/>

    <rect class="brand-mark" x="90" y="74" width="11" height="11"/>
    <text class="brand-name" x="107" y="85" font-size="17">VELL ROOFING</text>
    <text class="brand-url" x="134" y="141" font-size="13" text-anchor="middle">VELLROOFING.EXAMPLE</text>

    <text class="contact-title" x="34" y="267" font-size="15">VELL ROOFING</text>
    <text class="contact-line" x="34" y="312" font-size="14">VellRoofing.example</text>
    <text class="contact-line" x="34" y="332" font-size="14">555.672.VELL</text>
    <text class="contact-line" x="34" y="353" font-size="14">info@vellroofing.example</text>

    <rect class="stamp-box" x="494" y="69" width="92" height="109"/>
    <line class="address-line" x1="363" y1="255" x2="586" y2="255"/>
    <line class="address-line" x1="363" y1="304" x2="586" y2="304"/>
    <line class="address-line" x1="363" y1="353" x2="586" y2="353"/>
  </svg>

</main>
</body>
</html>
```